Ledgerforge Studio - WordPress Theme & Logo

Design a logo and Wordpress website design for Ledgerforge Studio. Ledgerforge Studio provides cryptocurrency development services to clients who need a team to create & continue developing a new cryptocurrency or who want to replace their current cryptocurrency development team. more details in the attached document.
Updates

Target Market(s)

Entrepreneurs who are building a business / platform that makes use of an underlying cryptocurrency.

Logo Text

LS or Ledgerforge Studio

Coding

Coded - Design and coding required

Font styles to use
Sans Serif

Requirements
Must have
• Professional logo, complete coded Wordpress theme for all pages, containing all specified links and buttons
Nice to have
• It would be nice if the buttons that are meant to integrate with Dealcurrent contain the necessary code for that. I can provide any necessary Dealcurrent details from my account.
Should not have
• Slow loading time

```html
<!DOCTYPE html>
<html lang="en">
<head>
<meta charset="utf-8">
<title>Ledgerforge Studio – Home Page Designs</title>
<link href="https://fonts.googleapis.com/css2?family=Poppins:wght@400;500;600;700&family=Roboto:wght@400;500;700&display=swap" rel="stylesheet">
<style>
:root{
  --board:#cbcbcb;
  --blue:#0d5bb0;
  --blue-dark:#0a4a93;
  --ink:#141414;
  --text:#333;
  --muted:#7a7a7a;
  --soft:#f3f3f3;
  --white:#fff;
  --star:#f4c20d;
}
*{box-sizing:border-box;margin:0;padding:0}
html,body{width:850px;height:1200px;overflow:hidden}
body{background:var(--board);font-family:'Roboto',Arial,sans-serif;color:var(--text);position:relative}
.brand-row{position:absolute;top:49px;left:0;width:850px;display:flex;justify-content:center;gap:28px}
.brand{display:flex;align-items:center;gap:6px;font-family:'Poppins',Arial,sans-serif;font-weight:600;font-size:7px;color:var(--ink)}
.brand-mark{width:17px;height:17px;border-radius:50%;background:var(--blue)}
.brand-mark.square{border-radius:2px}

.page{position:absolute;top:97px;width:671px;background:var(--white);transform:scale(.5234);transform-origin:0 0}
.page--a{left:57px}
.page--b{left:442px}

/* header */
.site-header{height:49px;position:relative;display:flex;align-items:center;padding:0 40px}
.site-logo{display:flex;align-items:center;gap:7px;font-family:'Poppins',Arial,sans-serif;font-weight:600;font-size:11px;color:var(--ink)}
.site-logo .brand-mark{width:22px;height:22px}
.nav{position:absolute;left:192px;top:0;height:49px;display:flex;align-items:center;gap:13px;font-size:8px;color:var(--ink)}
.nav .active{color:var(--blue)}
.btn{display:inline-flex;align-items:center;justify-content:center;gap:4px;background:var(--blue);color:var(--white);font-family:'Roboto',Arial,sans-serif;font-weight:500;font-size:8px;border-radius:12px;height:22px;padding:0 10px;white-space:nowrap}
.btn .arr{width:8px;height:8px;border-radius:50%;background:var(--white);display:inline-flex;align-items:center;justify-content:center}
.btn .arr::after{content:"";border-left:3px solid var(--blue);border-top:2px solid transparent;border-bottom:2px solid transparent;margin-left:1px}
.site-header .btn{position:absolute;left:499px;top:13px;width:134px;height:23px}

/* hero */
.hero{position:relative;color:var(--white);overflow:hidden}
.hero-art{position:absolute;inset:0}
.page--a .hero{height:369px}
.page--a .hero-art{background:radial-gradient(ellipse at 50% 20%,rgba(120,150,220,.55),transparent 60%),linear-gradient(180deg,#3b4f86 0%,#6b6487 35%,#3a4a78 55%,#1b2748 80%,#0f1830 100%)}
.page--b .hero{height:408px}
.page--b .hero-art{background:radial-gradient(circle at 72% 52%,rgba(70,150,230,.55),transparent 38%),radial-gradient(circle at 65% 62%,rgba(220,200,40,.35),transparent 18%),linear-gradient(120deg,#07152e 0%,#0d2a52 55%,#0a1f3f 100%)}
.hero h1{position:absolute;font-family:'Poppins',Arial,sans-serif;font-weight:400;font-size:20px;line-height:26px}
.hero h1 b{font-weight:700}
.hero p{position:absolute;font-size:7.5px;line-height:15px;font-weight:500}
.page--a .hero h1{left:0;right:0;top:109px;text-align:center}
.page--a .hero p{left:110px;right:110px;top:171px;text-align:center}
.page--a .hero .btn{position:absolute;left:264px;top:232px;width:143px}
.page--b .hero h1{left:60px;top:105px}
.page--b .hero p{left:60px;width:300px;top:195px;line-height:15.5px}
.page--b .hero .btn{position:absolute;left:61px;top:274px;width:142px}

/* section titles */
.section-title{position:absolute;left:0;right:0;text-align:center;font-family:'Poppins',Arial,sans-serif;font-weight:400;font-size:19px;color:var(--ink)}
.section-title b{font-weight:700}

/* why */
.why{position:relative;height:303px;background:linear-gradient(180deg,#fff 0%,#f7f8fa 60%,#fff 100%)}
.page--b .why{height:312px}
.why .section-title{top:47px}
.page--b .why .section-title{top:55px}
.why-cards{position:absolute;top:100px;left:76px;display:flex;gap:20px}
.page--b .why-cards{top:109px}
.why-card{width:160px;height:133px;background:var(--white);box-shadow:0 2px 8px rgba(0,0,0,.12);text-align:center;position:relative}
.why-card .ic{position:absolute;left:56px;top:15px;width:48px;height:48px;border-radius:50%;background:var(--blue);display:flex;align-items:center;justify-content:center}
.why-card h3{position:absolute;top:74px;left:0;right:0;font-size:10.5px;font-weight:500;color:var(--ink)}
.why-card p{position:absolute;top:94px;left:12px;right:12px;font-size:7px;line-height:13.5px;color:var(--muted)}

/* who */
.who{position:relative;height:219px;background:var(--soft)}
.who-photo{position:absolute;left:0;top:0;width:329px;height:219px;background:linear-gradient(135deg,#d9dde2 0%,#a9b0ba 40%,#3d4654 75%,#c9ccd0 100%)}
.who h2{position:absolute;left:360px;top:30px;font-family:'Poppins',Arial,sans-serif;font-weight:400;font-size:21px;color:var(--ink)}
.who h2 b{font-weight:700}
.who p{position:absolute;left:360px;top:69px;width:255px;font-size:7.2px;line-height:15px;color:var(--muted)}
.who .btn{position:absolute;left:360px;top:160px;width:92px}

/* clients */
.clients{position:relative;height:327px}
.clients .section-title{top:54px}
.quote-row{position:absolute;top:125px;left:62px;display:flex;gap:13px}
.quote{width:174px;position:relative}
.quote-card{height:107px;border:1px solid #e4e6ea;border-top:2px solid var(--blue);border-radius:8px 8px 4px 4px;box-shadow:0 3px 7px rgba(0,0,0,.08);background:var(--white);position:relative}
.quote-card::after{content:"";position:absolute;left:81px;bottom:-6px;width:10px;height:10px;background:var(--white);transform:rotate(45deg);border-right:1px solid #e4e6ea;border-bottom:1px solid #e4e6ea}
.quote-badge{position:absolute;left:63px;top:-24px;width:48px;height:48px;border-radius:50%;background:var(--white);box-shadow:0 1px 5px rgba(0,0,0,.15);display:flex;align-items:center;justify-content:center;z-index:1}
.quote-badge i{width:20px;height:20px;border-radius:50%;border:2px solid var(--blue)}
.page--a .quote:nth-child(2) .quote-badge i{border-color:#d8343c}
.page--a .quote:nth-child(3) .quote-badge i{border-color:#444;border-radius:3px}
.quote-badge.portrait{background:linear-gradient(180deg,#cfd3d8,#8e959e)}
.quote-card p{position:absolute;top:36px;left:12px;right:12px;text-align:center;font-size:7.3px;line-height:14.5px;color:#555}
.quote-name{position:absolute;top:118px;left:0;right:0;text-align:center;font-size:8px;font-weight:500;color:var(--ink)}
.quote-name small{font-size:5px;font-weight:400}
.stars{position:absolute;top:131px;left:0;right:0;text-align:center;color:var(--star);font-size:7px;letter-spacing:.5px}

/* services */
.services{position:relative;height:480px;background:var(--soft)}
.services .section-title{top:30px;font-size:20px}
.services .intro{position:absolute;left:65px;right:65px;text-align:center;font-size:7.2px;line-height:13.5px;color:var(--muted)}
.intro.one{top:64px}
.intro.two{top:98px}
.svc-mid{position:absolute;left:242px;top:158px;width:188px;height:205px;background:var(--white);border-radius:12px;border-bottom:3px solid var(--blue);box-shadow:0 4px 12px rgba(0,0,0,.08)}
.svc{position:absolute;top:171px;width:180px;text-align:center}
.svc:nth-of-type(1){left:51px}
.svc:nth-of-type(2){left:245px}
.svc:nth-of-type(3){left:439px}
.svc .ic{width:64px;height:64px;border-radius:50%;background:var(--blue);margin:0 auto;display:flex;align-items:center;justify-content:center}
.svc h3{margin-top:17px;font-size:9.8px;font-weight:500;color:var(--ink)}
.svc p{margin-top:6px;font-size:7.2px;line-height:14px;color:var(--muted)}
.svc .more{display:inline-flex;align-items:center;gap:4px;margin-top:6px;font-size:7.4px;font-weight:700;color:var(--blue)}
.svc .more .dot{width:7px;height:7px;border-radius:50%;background:var(--blue)}
.arrow{position:absolute;top:258px;width:14px;height:20px}
.arrow.prev{left:20px}
.arrow.next{left:632px}
.services .cta{position:absolute;left:264px;top:405px;width:144px}

/* footer */
.site-footer{position:relative;height:205px;background:var(--blue);color:var(--white)}
.site-footer h4{position:absolute;top:44px;font-size:10px;font-weight:700}
.contact{position:absolute;left:62px;top:70px;font-size:7.5px;line-height:13px;list-style:none}
.contact li{display:flex;gap:7px;margin-bottom:7px}
.contact svg{flex:none;margin-top:2px}
.links{position:absolute;top:69px;list-style:none;font-size:7.5px;line-height:15px}
.subscribe-field{position:absolute;left:400px;top:72px;width:132px;height:24px;border-radius:12px;background:var(--white);color:#999;font-size:6.5px;padding:8px 12px}
.submit{position:absolute;left:541px;top:72px;width:67px;height:24px;border-radius:12px;background:#0d1a2e;color:var(--white);font-weight:700;font-size:9px;display:flex;align-items:center;justify-content:center}
.consent{position:absolute;left:398px;top:111px;font-size:7px;font-weight:500;display:flex;gap:5px;align-items:center}
.socials{position:absolute;left:398px;top:133px;display:flex;gap:7px}
.socials i{width:17px;height:17px;border-radius:50%;border:1px solid rgba(255,255,255,.8)}
.footer-rule{position:absolute;left:62px;right:62px;top:168px;height:1px;background:rgba(255,255,255,.25)}
.copyright{position:absolute;left:0;right:0;top:184px;text-align:center;font-size:7px}
</style>
</head>
<body>

<div class="brand-row">
  <div class="brand"><span class="brand-mark"></span>Ledgerforge Studio</div>
  <div class="brand"><span class="brand-mark square"></span>Ledgerforge Studio</div>
</div>

<!-- Page design A -->
<section class="page page--a">
  <header class="site-header">
    <div class="site-logo"><span class="brand-mark"></span>Ledgerforge Studio</div>
    <nav class="nav"><span class="active">Home</span><span>About Us</span><span>Our Services</span><span>Service Tiers</span><span>Testimonials</span><span>Blog</span></nav>
    <a class="btn">Schedule a Free Consultation <span class="arr"></span></a>
  </header>
  <div class="hero">
    <div class="hero-art" role="img" aria-label="Night city skyline at dusk overlaid with a glowing network of connected nodes"></div>
    <h1><b>Your own cryptocurrency. Secure,</b> easy to<br>use, &amp; built by an expert team.</h1>
    <p>Ledgerforge Studio adds professionalism to cryptocurrency development. Our done-for-you service covers everything from development and IT operations to ongoing support. You have access to a full team, for less than the typical cost of a single developer.</p>
    <a class="btn">Schedule a Free Consultation <span class="arr"></span></a>
  </div>
  <div class="why">
    <h2 class="section-title"><b>Why choose</b> Ledgerforge Studio</h2>
    <div class="why-cards">
      <div class="why-card"><span class="ic"><svg width="24" height="20" viewBox="0 0 24 20" fill="none" stroke="#fff" stroke-width="1.4"><path d="M5 2h14l4 6-11 11L1 8z"/><path d="M1 8h22M8 2l-2 6 6 11 6-11-2-6"/></svg></span><h3>Value</h3><p>A team of experts, regular updates, and fixed costs</p></div>
      <div class="why-card"><span class="ic"><svg width="24" height="20" viewBox="0 0 24 20" fill="none" stroke="#fff" stroke-width="1.4"><path d="M5 2h14l4 6-11 11L1 8z"/><path d="M1 8h22M8 2l-2 6 6 11 6-11-2-6"/></svg></span><h3>Support</h3><p>Receive advice and other services, beyond development.</p></div>
      <div class="why-card"><span class="ic"><svg width="24" height="20" viewBox="0 0 24 20" fill="none" stroke="#fff" stroke-width="1.4"><path d="M5 2h14l4 6-11 11L1 8z"/><path d="M1 8h22M8 2l-2 6 6 11 6-11-2-6"/></svg></span><h3>Commitment</h3><p>Enjoy regular updates and new features.</p></div>
    </div>
  </div>
  <div class="who">
    <div class="who-photo" role="img" aria-label="Three colleagues working together at a laptop in a bright office"></div>
    <h2><b>Who</b> We Are</h2>
    <p>In addition to creating and enhancing cryptocurrencies for clients, the Ledgerforge Studio team has been running the Korvo cryptocurrency since 2017. We prefer long-term relationships, enabling us to deliver the very highest quality and giving you peace of mind that you've got aprofessional and trustworthy team at your side.</p>
    <a class="btn">READ MORE <span class="arr"></span></a>
  </div>
  <div class="clients">
    <h2 class="section-title"><b>What Our</b> Clients Say</h2>
    <div class="quote-row">
      <div class="quote"><span class="quote-badge"><i></i></span><div class="quote-card"><p>Sed ut perspiciatis unde omnis iste natus error sit voluptatem accusantium doloremque laudantium, totam rem aperiam, eaque ipsa</p></div><div class="quote-name">Dana Whitlow, <small>Chairman NVX</small></div><div class="stars">★★★★★</div></div>
      <div class="quote"><span class="quote-badge"><i></i></span><div class="quote-card"><p>Sed ut perspiciatis unde omnis iste natus error sit voluptatem accusantium doloremque laudantium, totam rem aperiam, eaque ipsa</p></div><div class="quote-name">Lena Okafor, <small>Project Manager</small></div><div class="stars">★★★★★</div></div>
      <div class="quote"><span class="quote-badge"><i></i></span><div class="quote-card"><p>Sed ut perspiciatis unde omnis iste natus error sit voluptatem accusantium doloremque laudantium, totam rem aperiam, eaque ipsa</p></div><div class="quote-name">Marco Selby, <small>Chairman NVX</small></div><div class="stars">★★★★★</div></div>
    </div>
  </div>
  <div class="services">
    <h2 class="section-title"><b>Our</b> Services</h2>
    <p class="intro one">Ledgerforge Studio provides a complete service that handles the development, IT operations and support for your cryptocurrency. Cryptocurrency development can be difficult and complex, and a quality development team is hard to find and expensive. expensive.</p>
    <p class="intro two">Ledgerforge Studio has an experienced team that has helped several clients launch and enhance their cryptocurrencies, including successfully running the Korvo cryptocurrency since 2017, and writing a next-generation cryptocurrency from scratch.</p>
    <div class="svc-mid"></div>
    <div class="svc"><span class="ic"><svg width="30" height="30" viewBox="0 0 30 30" fill="none" stroke="#fff" stroke-width="1.5"><rect x="8" y="3" width="14" height="24" rx="2"/><circle cx="15" cy="13" r="4"/><path d="M13 23h4"/></svg></span><h3>Blockchain Creation &amp; Launch</h3><p>Base fixed price for cryptocurrency development &amp; launch–would be customizable based on client requirements</p><span class="more">READ MORE <span class="dot"></span></span></div>
    <div class="svc"><span class="ic"><svg width="32" height="30" viewBox="0 0 32 30" fill="none" stroke="#fff" stroke-width="1.5"><rect x="5" y="6" width="22" height="15" rx="1"/><path d="M2 24h28"/><circle cx="16" cy="13" r="4"/></svg></span><h3>Basic offering</h3><p>Lower cost per month<br>Slower release schedule<br>Client assists with testing new releases<br>Less input into future roadmap/features</p><span class="more">READ MORE <span class="dot"></span></span></div>
    <div class="svc"><span class="ic"><svg width="32" height="30" viewBox="0 0 32 30" fill="none" stroke="#fff" stroke-width="1.5"><rect x="3" y="10" width="22" height="13" rx="1"/><circle cx="14" cy="16.5" r="3"/><circle cx="25" cy="21" r="5"/></svg></span><h3>Full service offering</h3><p>Mid-range cost per month<br>Releases every 1.5 - 2 months<br>Client can help request/prioritize new<br>Full testing by my team prior to release</p><span class="more">READ MORE <span class="dot"></span></span></div>
    <svg class="arrow prev" viewBox="0 0 14 20" fill="none" stroke="#9a9a9a" stroke-width="2"><path d="M11 2 3 10l8 8"/></svg>
    <svg class="arrow next" viewBox="0 0 14 20" fill="none" stroke="#9a9a9a" stroke-width="2"><path d="m3 2 8 8-8 8"/></svg>
    <a class="btn cta">Schedule a Free Consultation <span class="arr"></span></a>
  </div>
  <footer class="site-footer">
    <h4 style="left:62px">Contact Us</h4>
    <ul class="contact">
      <li><svg width="7" height="9" viewBox="0 0 7 9"><path d="M3.5 0A3.5 3.5 0 0 0 0 3.5C0 6 3.5 9 3.5 9S7 6 7 3.5A3.5 3.5 0 0 0 3.5 0z" fill="#fff"/></svg>3501 Lorem ipsum dolor sit<br>amet, consectetur</li>
      <li><svg width="8" height="6" viewBox="0 0 8 6"><rect width="8" height="6" fill="#fff"/><path d="m0 0 4 3 4-3" stroke="#0d5bb0" fill="none"/></svg>hello@ledgerforgestudio.com</li>
      <li><svg width="7" height="7" viewBox="0 0 7 7"><path d="M1 0 2.5 2 1.5 3a5 5 0 0 0 2.5 2.5l1-1L7 6 6 7C3 7 0 4 0 1z" fill="#fff"/></svg>325.555.0142</li>
      <li><svg width="8" height="7" viewBox="0 0 8 7"><rect y="2" width="8" height="5" fill="#fff"/><rect x="2" width="4" height="2" fill="#fff"/></svg>(888) 555 - 0199</li>
    </ul>
    <h4 style="left:221px">Links</h4>
    <ul class="links" style="left:221px"><li>Home</li><li>About Us</li><li>Our Services</li><li>Service Tiers</li><li>Testimonials</li></ul>
    <ul class="links" style="left:292px"><li>Terms &amp; Condition</li><li>Privacy Policy</li><li>Updates</li><li>Support</li><li>Contact</li></ul>
    <h4 style="left:398px">Subscribe for Updates</h4>
    <div class="subscribe-field">Emaill Address</div>
    <div class="submit">SUBMIT</div>
    <div class="consent"><svg width="7" height="7" viewBox="0 0 7 7" fill="none" stroke="#fff" stroke-width="1.2"><path d="m1 3.5 2 2 3-4"/></svg>Yes, Please Contact me.</div>
    <div class="socials"><i></i><i></i><i></i></div>
    <div class="footer-rule"></div>
    <div class="copyright">© 2021 Ledgerforge Studio &nbsp;|&nbsp; All Rights Reserved</div>
  </footer>
</section>

<!-- Page design B -->
<section class="page page--b">
  <header class="site-header">
    <div class="site-logo"><span class="brand-mark square"></span>Ledgerforge Studio</div>
    <nav class="nav"><span class="active">Home</span><span>About Us</span><span>Our Services</span><span>Service Tiers</span><span>Testimonials</span><span>Blog</span></nav>
    <a class="btn">Schedule a Free Consultation <span class="arr"></span></a>
  </header>
  <div class="hero">
    <div class="hero-art" role="img" aria-label="Glowing wireframe cubes with neon blue and gold edges floating in dark space"></div>
    <h1><b>Your own cryptocurrency.<br>Secure,</b> easy to use, &amp; built<br>by an expert team.</h1>
    <p>Ledgerforge Studio adds professionalism to cryptocurrency development. Our done-for-you service covers everything from development and IT operations to ongoing support. You have access to a full team, for less than the typical cost of a single developer.</p>
    <a class="btn">Schedule a Free Consultation <span class="arr"></span></a>
  </div>
  <div class="why">
    <h2 class="section-title"><b>Why choose</b> Ledgerforge Studio</h2>
    <div class="why-cards">
      <div class="why-card"><span class="ic"><svg width="24" height="20" viewBox="0 0 24 20" fill="none" stroke="#fff" stroke-width="1.4"><path d="M5 2h14l4 6-11 11L1 8z"/><path d="M1 8h22M8 2l-2 6 6 11 6-11-2-6"/></svg></span><h3>Value</h3><p>A team of experts, regular updates, and fixed costs</p></div>
      <div class="why-card"><span class="ic"><svg width="24" height="20" viewBox="0 0 24 20" fill="none" stroke="#fff" stroke-width="1.4"><path d="M5 2h14l4 6-11 11L1 8z"/><path d="M1 8h22M8 2l-2 6 6 11 6-11-2-6"/></svg></span><h3>Support</h3><p>Receive advice and other services, beyond development.</p></div>
      <div class="why-card"><span class="ic"><svg width="24" height="20" viewBox="0 0 24 20" fill="none" stroke="#fff" stroke-width="1.4"><path d="M5 2h14l4 6-11 11L1 8z"/><path d="M1 8h22M8 2l-2 6 6 11 6-11-2-6"/></svg></span><h3>Commitment</h3><p>Enjoy regular updates and new features.</p></div>
    </div>
  </div>
  <div class="who">
    <div class="who-photo" role="img" aria-label="Three colleagues working together at a laptop in a bright office"></div>
    <h2><b>Who</b> We Are</h2>
    <p>In addition to creating and enhancing cryptocurrencies for clients, the Ledgerforge Studio team has been running the Korvo cryptocurrency since 2017. We prefer long-term relationships, enabling us to deliver the very highest quality and giving you peace of mind that you've got aprofessional and trustworthy team at your side.</p>
    <a class="btn">READ MORE <span class="arr"></span></a>
  </div>
  <div class="clients">
    <h2 class="section-title"><b>What Our</b> Clients Say</h2>
    <div class="quote-row">
      <div class="quote"><span class="quote-badge portrait" role="img" aria-label="Client portrait"></span><div class="quote-card"><p>Sed ut perspiciatis unde omnis iste natus error sit voluptatem accusantium doloremque laudantium, totam rem aperiam, eaque ipsa</p></div><div class="quote-name">Dana Whitlow, <small>Chairman NVX</small></div><div class="stars">★★★★★</div></div>
      <div class="quote"><span class="quote-badge portrait" role="img" aria-label="Client portrait"></span><div class="quote-card"><p>Sed ut perspiciatis unde omnis iste natus error sit voluptatem accusantium doloremque laudantium, totam rem aperiam, eaque ipsa</p></div><div class="quote-name">Lena Okafor, <small>Project Manager</small></div><div class="stars">★★★★★</div></div>
      <div class="quote"><span class="quote-badge portrait" role="img" aria-label="Client portrait"></span><div class="quote-card"><p>Sed ut perspiciatis unde omnis iste natus error sit voluptatem accusantium doloremque laudantium, totam rem aperiam, eaque ipsa</p></div><div class="quote-name">Marco Selby, <small>Chairman NVX</small></div><div class="stars">★★★★★</div></div>
    </div>
  </div>
  <div class="services">
    <h2 class="section-title"><b>Our</b> Services</h2>
    <p class="intro one">Ledgerforge Studio provides a complete service that handles the development, IT operations and support for your cryptocurrency. Cryptocurrency development can be difficult and complex, and a quality development team is hard to find and expensive. expensive.</p>
    <p class="intro two">Ledgerforge Studio has an experienced team that has helped several clients launch and enhance their cryptocurrencies, including successfully running the Korvo cryptocurrency since 2017, and writing a next-generation cryptocurrency from scratch.</p>
    <div class="svc-mid"></div>
    <div class="svc"><span class="ic"><svg width="30" height="30" viewBox="0 0 30 30" fill="none" stroke="#fff" stroke-width="1.5"><rect x="8" y="3" width="14" height="24" rx="2"/><circle cx="15" cy="13" r="4"/><path d="M13 23h4"/></svg></span><h3>Blockchain Creation &amp; Launch</h3><p>Base fixed price for cryptocurrency development &amp; launch–would be customizable based on client requirements</p><span class="more">READ MORE <span class="dot"></span></span></div>
    <div class="svc"><span class="ic"><svg width="32" height="30" viewBox="0 0 32 30" fill="none" stroke="#fff" stroke-width="1.5"><rect x="5" y="6" width="22" height="15" rx="1"/><path d="M2 24h28"/><circle cx="16" cy="13" r="4"/></svg></span><h3>Basic offering</h3><p>Lower cost per month<br>Slower release schedule<br>Client assists with testing new releases<br>Less input into future roadmap/features</p><span class="more">READ MORE <span class="dot"></span></span></div>
    <div class="svc"><span class="ic"><svg width="32" height="30" viewBox="0 0 32 30" fill="none" stroke="#fff" stroke-width="1.5"><rect x="3" y="10" width="22" height="13" rx="1"/><circle cx="14" cy="16.5" r="3"/><circle cx="25" cy="21" r="5"/></svg></span><h3>Full service offering</h3><p>Mid-range cost per month<br>Releases every 1.5 - 2 months<br>Client can help request/prioritize new<br>Full testing by my team prior to release</p><span class="more">READ MORE <span class="dot"></span></span></div>
    <svg class="arrow prev" viewBox="0 0 14 20" fill="none" stroke="#9a9a9a" stroke-width="2"><path d="M11 2 3 10l8 8"/></svg>
    <svg class="arrow next" viewBox="0 0 14 20" fill="none" stroke="#9a9a9a" stroke-width="2"><path d="m3 2 8 8-8 8"/></svg>
    <a class="btn cta">Schedule a Free Consultation <span class="arr"></span></a>
  </div>
  <footer class="site-footer">
    <h4 style="left:62px">Contact Us</h4>
    <ul class="contact">
      <li><svg width="7" height="9" viewBox="0 0 7 9"><path d="M3.5 0A3.5 3.5 0 0 0 0 3.5C0 6 3.5 9 3.5 9S7 6 7 3.5A3.5 3.5 0 0 0 3.5 0z" fill="#fff"/></svg>3501 Lorem ipsum dolor sit<br>amet, consectetur</li>
      <li><svg width="8" height="6" viewBox="0 0 8 6"><rect width="8" height="6" fill="#fff"/><path d="m0 0 4 3 4-3" stroke="#0d5bb0" fill="none"/></svg>hello@ledgerforgestudio.com</li>
      <li><svg width="7" height="7" viewBox="0 0 7 7"><path d="M1 0 2.5 2 1.5 3a5 5 0 0 0 2.5 2.5l1-1L7 6 6 7C3 7 0 4 0 1z" fill="#fff"/></svg>325.555.0142</li>
      <li><svg width="8" height="7" viewBox="0 0 8 7"><rect y="2" width="8" height="5" fill="#fff"/><rect x="2" width="4" height="2" fill="#fff"/></svg>(888) 555 - 0199</li>
    </ul>
    <h4 style="left:221px">Links</h4>
    <ul class="links" style="left:221px"><li>Home</li><li>About Us</li><li>Our Services</li><li>Service Tiers</li><li>Testimonials</li></ul>
    <ul class="links" style="left:292px"><li>Terms &amp; Condition</li><li>Privacy Policy</li><li>Updates</li><li>Support</li><li>Contact</li></ul>
    <h4 style="left:398px">Subscribe for Updates</h4>
    <div class="subscribe-field">Emaill Address</div>
    <div class="submit">SUBMIT</div>
    <div class="consent"><svg width="7" height="7" viewBox="0 0 7 7" fill="none" stroke="#fff" stroke-width="1.2"><path d="m1 3.5 2 2 3-4"/></svg>Yes, Please Contact me.</div>
    <div class="socials"><i></i><i></i><i></i></div>
    <div class="footer-rule"></div>
    <div class="copyright">© 2021 Ledgerforge Studio &nbsp;|&nbsp; All Rights Reserved</div>
  </footer>
</section>

</body>
</html>
```